Business Identity Stationary

Already have the logo which is in the attached files so only need the Business STationary
1) Double Sided Business Card
2) Letterhead
3) Presentation folder with business card holder on inside cover
4) WIth compliments slip
See information for business cards, letterhead and presentation folder below.

This should be a simply job using a logo we already had designed along with a little device. I suggest using the device off center and perhaps lower in the corner in an abstract way. Also the logo device could be used as a watermark for the letterhead. The designer who created the logo presented something that I think works well for a business card. The front of the double sided business card could have the name logo small for the website address and only use the Lime device on the front. Then on the back could be the name Parvel Advisory logo.

Please note that for the business card the black and lime green background do look good. Also please think of using the lime device separately in an unusual way.

It has been brought to my attention that.my budget was far to low. Hopefully this.will attract you to the project. 

The parent company of Parvel Advisory is BrightHeron holdings. I have uploaded a file of the Bright Heron business card I really like. Perhaps use this business card as a guide to the type of modern and clean style I am looking for. It also works to have the Parvel Advisroy and Bright Heron similar.

Industry/Entity Type

Business

Font styles to use
Sans Serif

Colors
9bcb3c
000000
5c5c5c
add136
cadf82
eaf2cf
f9fbf2
1b1b1b
757575

Requirements
Must have
• 1) Double Sided Business Card
Renata Tolberg
Director
Tel: +505 8426 3057
Email: rtb@parveladvisory.com
Website: www.parveladvisory.com

Gregory Tolberg
Director
Tel: +505 8426 3092
Email: gkb@parveladvisory.com

Helena Pardo Duvignac
Director
Tel: 8342 1168
Email: hpd@parveladvisory.com

2) Letterhead
Logo
Lime Logo Device
Website Address: www.parveladvisory.com
Small print on bottom: Parvel Advisory a Bright Heron Holding Company SA. RUC K0470000283914

3) Presentation Folder
Traditional Presentation folder with inside front cover spot for the insertion of business card.

4) With Compliments slip

```html
<!DOCTYPE html>
<html lang="en">
<head>
<meta charset="utf-8">
<title>Parvel Advisory – Business Stationery</title>
<link href="https://fonts.googleapis.com/css2?family=Questrial&display=swap" rel="stylesheet">
<style>
  :root {
    --canvas: #e6e6e6;
    --green: #418301;
    --green-text: #3b7a00;
    --paper: #ffffff;
    --ink: #333333;
    --shadow: 3px 3px 4px rgba(0,0,0,0.45);
  }
  * { margin: 0; padding: 0; box-sizing: border-box; }
  html, body { width: 1200px; height: 1000px; overflow: hidden; }
  body {
    background: var(--canvas);
    position: relative;
    font-family: "Questrial", "Trebuchet MS", sans-serif;
    color: var(--ink);
  }
  .sheet { position: absolute; background: var(--paper); box-shadow: var(--shadow); overflow: hidden; }
  .band { position: absolute; left: 0; right: 0; background: var(--green); }
  .wordmark { position: absolute; color: #fff; font-weight: 400; white-space: nowrap; letter-spacing: 0.5px; }

  /* Letterhead */
  .letterhead { left: 28px; top: 34px; width: 368px; height: 474px; }
  .letterhead .head { top: 0; height: 34px; }
  .letterhead .wordmark { left: 8px; top: 8px; font-size: 16px; }
  .letterhead .foot { bottom: 0; height: 8px; }
  .small-print { position: absolute; left: 0; right: 0; text-align: center; font-size: 6px; color: #222; line-height: 9px; }
  .letterhead .small-print { top: 447px; }

  /* Presentation folder */
  .folder { left: 427px; top: 34px; width: 753px; height: 474px; }
  .folder .outer { position: absolute; left: 0; top: 0; width: 377px; height: 474px; background: var(--green); }
  .folder .outer .small-print { top: 454px; color: #fff; font-size: 5.5px; line-height: 8px; }
  .folder .head { left: 377px; top: 0; height: 92px; }
  .folder .wordmark { left: 398px; top: 28px; font-size: 30px; }
  .folder .foot { left: 377px; bottom: 0; height: 8px; }
  .card-slot { position: absolute; left: 586px; top: 202px; width: 156px; height: 100px; border: 1px solid #777; background: var(--paper); }
  .card-slot .head { left: 5px; right: 5px; top: 5px; height: 27px; }
  .card-slot .wordmark { left: 9px; top: 11px; font-size: 10px; }
  .card-slot .foot { left: 5px; right: 5px; bottom: 5px; height: 6px; }
  .mini-details { position: absolute; left: 8px; top: 42px; font-size: 5.5px; line-height: 7.5px; color: var(--green-text); }
  .mini-details .name { font-size: 6.5px; }

  /* Compliments slip */
  .slip { left: 295px; top: 527px; width: 570px; height: 260px; }
  .slip .head { top: 0; height: 54px; }
  .slip .wordmark { left: 14px; top: 14px; font-size: 26px; }
  .slip .greeting { position: absolute; left: 58px; top: 84px; font-size: 9px; }
  .slip .web { position: absolute; left: 9px; top: 236px; font-size: 9px; }
  .slip .foot { bottom: 0; height: 12px; }

  /* Business cards */
  .card { top: 809px; width: 279px; height: 172px; }
  .card-back { left: 25px; top: 808px; width: 280px; height: 173px; background: var(--green); }
  .card-back .wordmark { left: 0; right: 0; top: 70px; text-align: center; font-size: 27px; }
  .card-front .head { top: 0; height: 51px; }
  .card-front .wordmark { left: 14px; top: 12px; font-size: 24px; }
  .card-front .foot { bottom: 2px; height: 11px; }
  .card-front.renata { left: 321px; }
  .card-front.gregory { left: 612px; }
  .card-front.helena { left: 902px; }
  .holder { position: absolute; left: 7px; top: 72px; color: var(--green-text); }
  .holder .name { font-size: 12px; }
  .holder .role { font-size: 10px; margin-top: 3px; }
  .contact { list-style: none; margin-top: 6px; font-size: 9.5px; }
  .contact li { display: flex; align-items: center; height: 14.5px; }
  .contact svg { width: 12px; height: 10px; margin-right: 8px; fill: var(--green); }
</style>
</head>
<body>

<!-- Letterhead -->
<section class="sheet letterhead" aria-label="Letterhead">
  <div class="band head"></div>
  <span class="wordmark">Parvel Advisory</span>
  <p class="small-print">www.parveladvisory.com<br>Parvel Advisory a Bright Heron Holding Company SA. RUC K0470000283914</p>
  <div class="band foot"></div>
</section>

<!-- Presentation folder -->
<section class="sheet folder" aria-label="Presentation folder">
  <div class="outer">
    <p class="small-print">www.parveladvisory.com<br>Parvel Advisory a Bright Heron Holding Company SA. RUC K0470000283914</p>
  </div>
  <div class="band head"></div>
  <span class="wordmark">Parvel Advisory</span>
  <div class="card-slot">
    <div class="band head"></div>
    <span class="wordmark">Parvel Advisory</span>
    <div class="mini-details">
      <div class="name">Renata Tolberg</div>
      <div>Director</div>
      <div>rtb@parveladvisory.com</div>
      <div>+505 8426 3057</div>
      <div>www.parveladvisory.com</div>
    </div>
    <div class="band foot"></div>
  </div>
  <div class="band foot"></div>
</section>

<!-- With compliments slip -->
<section class="sheet slip" aria-label="With compliments slip">
  <div class="band head"></div>
  <span class="wordmark">Parvel Advisory</span>
  <p class="greeting">With Compliments,</p>
  <p class="web">www.parveladvisory.com</p>
  <div class="band foot"></div>
</section>

<!-- Business card back -->
<section class="sheet card-back" aria-label="Business card back">
  <span class="wordmark">Parvel Advisory</span>
</section>

<svg width="0" height="0" style="position:absolute" aria-hidden="true">
  <symbol id="icon-mail" viewBox="0 0 12 10"><path d="M0 1h12v8H0z M1 2l5 3.5L11 2" fill="currentColor"/><path d="M1 2.2l5 3.4 5-3.4" stroke="#fff" stroke-width="1" fill="none"/></symbol>
  <symbol id="icon-phone" viewBox="0 0 12 10"><rect x="3.5" y="0" width="5" height="10" rx="1"/><rect x="4.5" y="1.5" width="3" height="4" fill="#fff"/></symbol>
  <symbol id="icon-web" viewBox="0 0 12 10"><circle cx="6" cy="5" r="4.5"/><path d="M1.5 5h9M6 .5v9" stroke="#fff" stroke-width="0.8"/></symbol>
</svg>

<!-- Business card fronts -->
<section class="sheet card card-front renata" aria-label="Business card, Renata Tolberg">
  <div class="band head"></div>
  <span class="wordmark">Parvel Advisory</span>
  <div class="holder">
    <div class="name">Renata Tolberg</div>
    <div class="role">Director</div>
    <ul class="contact">
      <li><svg><use href="#icon-mail"/></svg>rtb@parveladvisory.com</li>
      <li><svg><use href="#icon-phone"/></svg>+505 8426 3057</li>
      <li><svg><use href="#icon-web"/></svg>www.parveladvisory.com</li>
    </ul>
  </div>
  <div class="band foot"></div>
</section>

<section class="sheet card card-front gregory" aria-label="Business card, Gregory Tolberg">
  <div class="band head"></div>
  <span class="wordmark">Parvel Advisory</span>
  <div class="holder">
    <div class="name">Gregory Tolberg</div>
    <div class="role">Director</div>
    <ul class="contact">
      <li><svg><use href="#icon-mail"/></svg>gkb@parveladvisory.com</li>
      <li><svg><use href="#icon-phone"/></svg>+505 8426 3092</li>
      <li><svg><use href="#icon-web"/></svg>www.parveladvisory.com</li>
    </ul>
  </div>
  <div class="band foot"></div>
</section>

<section class="sheet card card-front helena" aria-label="Business card, Helena Pardo Duvignac">
  <div class="band head"></div>
  <span class="wordmark">Parvel Advisory</span>
  <div class="holder">
    <div class="name">Helena Pardo Duvignac</div>
    <div class="role">Director</div>
    <ul class="contact">
      <li><svg><use href="#icon-mail"/></svg>hpd@parveladvisory.com</li>
      <li><svg><use href="#icon-phone"/></svg>+505 8342 1168</li>
      <li><svg><use href="#icon-web"/></svg>www.parveladvisory.com</li>
    </ul>
  </div>
  <div class="band foot"></div>
</section>

</body>
</html>
```